Landing Page Design für Tor- und Zaunbaufirma
Zielgruppe
der Kunde ist eine Tor- und Zaunbaufirma. Die Zielgruppen sind private Häuslebauer und Firmen.
Aufgabenstellung
Die Farben des Logos sollen nur sehr sparsam eingesetzt werden.
Die Navigation soll sich an der jetzigen Webseite orientieren. www.frenk-gitterwerk.de
Impressum und Datenschutz dezenter platzieren
Kommunikationsdaten vordergründig darstellen
mehr als 25-Jahre Erfahrung im Tor- und Zaunbau
Regionalität beachten

```html
<!DOCTYPE html>
<html lang="de">
<head>
<meta charset="utf-8">
<title>Tor &amp; Zaunbau Frenk – Chemnitz</title>
<link rel="stylesheet" href="https://fonts.googleapis.com/css2?family=Montserrat:wght@400;500;700;800&family=Noto+Serif:wght@400&display=swap">
<style>
:root{
  --magenta:#e6007e;
  --yellow:#fff200;
  --olive:#b5ad0f;
  --navy:#232d3d;
  --ink:#2a2a2a;
  --muted:#555;
  --white:#fff;
  --rule:#c9c9c9;
}
*{margin:0;padding:0;box-sizing:border-box}
html,body{width:1200px;height:2244px;overflow:hidden;background:var(--white)}
body{position:relative;font-family:"Montserrat",sans-serif;color:var(--ink)}
.abs{position:absolute}

.brand{left:94px;top:95px;width:262px;height:95px;display:flex;align-items:center;gap:12px}
.brand-mark{width:22px;height:22px;background:var(--magenta)}
.brand-name{font-weight:800;font-size:24px;color:var(--magenta);line-height:1.1}
.tagline{right:91px;top:110px;text-align:right;font-family:"Noto Serif",serif;font-size:24px;line-height:29px;color:var(--magenta)}

.main-nav{left:92px;top:237px;width:1016px;height:58px;display:flex;font-size:21px}
.main-nav a{display:flex;align-items:center;justify-content:center;color:var(--ink);text-decoration:none;height:100%;position:relative}
.main-nav a+a::before{content:"";position:absolute;left:0;top:6px;bottom:6px;width:1px;background:var(--rule)}
.main-nav .active{background:var(--magenta);color:var(--white);width:198px}
.main-nav .active::before{display:none}
.caret{margin-left:4px}

.hero{left:92px;top:295px;width:1016px;height:408px;background:linear-gradient(100deg,#6a5a4a 0%,#c27a45 22%,#3b3430 45%,#2a2624 70%,#4a3f38 100%);overflow:hidden}
.hero-title{left:0;width:100%;top:90px;text-align:center;color:var(--yellow);font-weight:800;font-size:42px}
.hero-sub{left:0;width:100%;top:152px;text-align:center;color:var(--white);font-size:18px;letter-spacing:2.4px;line-height:38px}
.hero-badge{left:133px;top:271px;width:750px;height:62px;background:var(--olive);color:var(--white);font-weight:700;font-size:24px;display:flex;align-items:center;justify-content:center}

.carousel-arrow{top:910px;width:24px;height:48px}
.product{top:784px;width:245px;height:245px;box-shadow:2px 3px 6px rgba(0,0,0,.25)}
.product-label{top:1046px;width:245px;text-align:center;font-size:16px;font-weight:700;letter-spacing:.5px;color:#222}
.product-label.current{color:var(--magenta)}

.strengths{left:92px;top:1121px;width:1016px;height:275px;background:linear-gradient(90deg,#2a2118 0%,#4a3a28 40%,#3a2f22 70%,#221a12 100%);color:var(--white)}
.strengths h2{font-size:21px;font-weight:700;color:var(--yellow);position:absolute;top:38px}
.strengths p{font-size:16px;line-height:23px;position:absolute;top:94px}
.strengths .col-a{left:43px}
.strengths .col-b{left:514px}
.strengths p.col-b{line-height:25.5px}

.about-rule{left:832px;top:1455px;width:259px;height:1px;background:#999}
.about-text{left:92px;top:1492px;width:720px;font-size:16px;line-height:25.5px;color:var(--muted)}
.btn-more{left:92px;top:1638px;width:149px;height:57px;background:var(--navy);color:var(--white);font-size:16px;display:flex;align-items:center;justify-content:center;letter-spacing:.3px}
.portrait{left:871px;top:1475px;width:220px;height:220px;background:linear-gradient(180deg,#f2f2f2 0%,#e6e4e0 60%,#dcdde2 100%)}

.site-footer{left:92px;top:1788px;width:1016px;height:362px;background:var(--navy);color:#d6d9de;font-size:17px}
.site-footer ul{list-style:none;position:absolute}
.site-footer li{height:37.5px}
.site-footer .hl{color:var(--yellow)}
.foot-nav{left:33px;top:66px}
.foot-services{left:233px;top:64px}
.foot-divider{left:631px;top:66px;width:2px;height:230px;background:#6a7383}
.foot-contact{left:705px;top:62px;font-size:19px;line-height:37.5px}
</style>
</head>
<body>

<header>
  <div class="abs brand" aria-label="Tor &amp; Zaunbau Frenk">
    <span class="brand-mark"></span>
    <span class="brand-name">Tor &amp; Zaunbau<br>Frenk</span>
  </div>
  <p class="abs tagline">Der richtige “Rahmen” Für Ihr<br>privates oder gewerbliches Grundstück</p>
</header>

<nav class="abs main-nav">
  <a class="active" href="#">Über uns</a>
  <a href="#" style="width:274px">Unsere Leistungen<svg class="caret" width="14" height="10" viewBox="0 0 14 10"><path d="M1 2l6 6 6-6" fill="none" stroke="#e6007e" stroke-width="3"/></svg></a>
  <a href="#" style="width:158px">Kontakt</a>
  <a href="#" style="width:192px">Impressum</a>
  <a href="#" style="width:194px">Datenschutz</a>
</nav>

<section class="abs hero" role="img" aria-label="Foto eines Metallzauns im Abendlicht">
  <h1 class="abs hero-title">Tor &amp; Zaunbau Frenk aus Chemnitz</h1>
  <p class="abs hero-sub">Ihr Partner für alle Zaun- und Torsysteme<br>in den Regionen Chemnitz und Zwickau</p>
  <div class="abs hero-badge">Mehr als 25-Jahre Erfahrung im Tor- und Zaunbau</div>
</section>

<section aria-label="Leistungen">
  <svg class="abs carousel-arrow" style="left:170px" viewBox="0 0 24 48"><path d="M18 6L6 24l12 18" fill="none" stroke="#2b3242" stroke-width="5"/></svg>
  <svg class="abs carousel-arrow" style="left:1005px" viewBox="0 0 24 48"><path d="M6 6l12 18L6 42" fill="none" stroke="#2b3242" stroke-width="5"/></svg>

  <div class="abs product" style="left:225px;background:linear-gradient(180deg,#b9d3e6 0%,#b9d3e6 28%,#8a949c 45%,#7a8690 100%)" role="img" aria-label="Foto einer Sichtschutzanlage aus Metalllamellen"></div>
  <div class="abs product" style="left:539px;background:linear-gradient(180deg,#c8c6bf 0%,#8e8a80 50%,#5a5040 80%,#2a2620 100%)" role="img" aria-label="Foto eines Metallzauns mit goldenen Spitzen vor einem Schloss"></div>
  <div class="abs product" style="left:852px;width:123px;box-shadow:none;background:linear-gradient(180deg,#cfe0ea 0%,#9aa8b0 35%,#7e97a3 60%,#f2f2f2 85%,#cdd2c8 100%)" role="img" aria-label="Foto eines weißen Holzzauns vor einem Haus"></div>

  <p class="abs product-label current" style="left:225px">SICHTSCHUTZANLAGEN</p>
  <p class="abs product-label" style="left:539px">METALLZÄUNE</p>
  <p class="abs product-label" style="left:852px;width:123px;overflow:hidden;text-align:left;padding-left:69px;white-space:nowrap">HOLZZÄUNE</p>
</section>

<section class="abs strengths" role="img" aria-label="Hintergrundfoto eines Holztors im Abendlicht">
  <h2 class="col-a">Unsere Stärken:</h2>
  <p class="col-a">schlüsselfertige Erstellung komplexer Toranlagen<br>schmuckvolle und zweckmäßige Zäune<br>Dreh- und Schiebetore<br>elektrische Torantriebe<br>Briefkastenanlagen</p>
  <h2 class="col-b">Über Das Produkt</h2>
  <p class="col-b">Wenn es um Zäune, Toranlagen, Schranken geht,<br>ob als Objektschutz  für Industrieanlagen, als Lärmschutz<br>für öffentliche Einrichtungen oder ganz einfach<br>als Schmuck und Schutz vor Einblicken im Privatbereich<br>– bei Tor &amp; Zaunbau Frenk können<br>Sie sich auf einen Rund-Um-Service verlassen</p>
</section>

<section aria-label="Über uns">
  <div class="abs about-rule"></div>
  <p class="abs about-text">Von der Beratung und Planung über Fertigung und  Montage bis hin zu Service<br>und Wartung haben Sie in uns einen direkten Ansprechpartner.<br>Lassen Sie sich auf den folgenden Seiten überraschen und anregen von der Vielfalt<br>der Möglichkeiten und den Beispielen unserer Arbeiten.</p>
  <a class="abs btn-more">ZEIG MEHR</a>
  <div class="abs portrait" role="img" aria-label="Porträtfoto des Geschäftsführers"></div>
</section>

<footer class="abs site-footer">
  <ul class="foot-nav">
    <li class="hl">Über uns</li>
    <li>Kontakt</li>
    <li>Impressum</li>
    <li style="margin-top:4px">Datenschutz</li>
  </ul>
  <ul class="foot-services">
    <li class="hl">Drehflügeltore</li>
    <li>Schiebetore</li>
    <li>Sichtschutzanlagen</li>
    <li style="margin-top:4px">Holzzäune</li>
    <li>Metallzäune</li>
    <li>Elektr. Torantriebe &amp; Briefkastenanlagen</li>
    <li>Gartenaccessoires</li>
  </ul>
  <div class="abs foot-divider"></div>
  <address class="abs foot-contact" style="font-style:normal">
    Tor &amp; Zaunbau Frenk<br>Lindenauer Str. 42<br>09124 Chemnitz<br><br>
    Tel. 0371 / 555 14 20<br>Mobil 0172 / 555 39 81<br>Fax 0371 / 555 14 21
  </address>
</footer>

</body>
</html>
```